Website Wordpress Responsive Design and Development - Landscape Company

Site is currently under construction, but the old site needs a refresh.
Need a fully responsive wordpress website (built in Elementor or comparable theme).
Here's the way it looked prior :
https://pastpages.example/snap/20220330041341/http://brookmoorgreens.example/
Their current designer came up with a website sample and it looks terrible :
https://talkowenpics.sitebuild.example/mysite/projects
Websites the client likes for some inspiration, but needs better than these :
https://www.quarrinbeckgroundworkers.example/
http://kvatelierpx.example/
https://tullidgepartners.example/
https://www.garbettcoinc.example/

Navigation includes :
• Home
• Complete structure of website content is available in the home page, yielding main information on services.
• Visually appealing but simple to use and navigate. Subtle amount of content, but enough for search engines to be able to read up the target phrases.
• Sections on the home page include :
▪ About - Information about the company and main service focus
▪ Gallery - Imagery categorized to include lightbox style zoom.
▪ Contact - Contact details and connection information
• About
• Bannered header
• Content appropriately formatted to subject
• Gallery
• Bannered header
• Each of the albums would have their own categorized image content
• Contact
• Bannered header
• Social Media connector available on all pages (like box, feed, etc) if applicable
• Content can be updated on all pages
• Basic Optimization for SEO with title tags, meta data where applicable.
• Google Analytics and Sitemap installed. (google account will be provided)
• Google Business Listing and Search Console Accounts created

Coded - Design and coding required

1 page

• Wordpress Responsive Design

```html
<!DOCTYPE html>
<html lang="en">
<head>
<meta charset="UTF-8">
<title>Brookmoor Greens, Inc — Portfolio</title>
<link rel="stylesheet" href="https://fonts.googleapis.com/css2?family=Inter:wght@300;400;500;600&display=swap">
<style>
  :root {
    --white: #ffffff;
    --accent-green: #4fc36a;
    --sky: #5f7a90;
    --foliage-dark: #1d3318;
    --foliage-mid: #34561f;
    --lawn: #4e7a25;
    --shade: rgba(8, 14, 10, 0.38);
  }
  * { margin: 0; padding: 0; box-sizing: border-box; }
  html, body { width: 1200px; height: 675px; overflow: hidden; }
  body { font-family: "Inter", sans-serif; color: var(--white); background: var(--foliage-dark); }

  .hero { position: relative; width: 1200px; height: 675px; overflow: hidden; }

  .hero-photo {
    position: absolute; inset: 0;
    background:
      radial-gradient(ellipse at 92% 45%, rgba(70, 100, 110, 0.55), transparent 30%),
      radial-gradient(ellipse at 70% 65%, rgba(110, 150, 40, 0.45), transparent 40%),
      linear-gradient(180deg, var(--sky) 0%, #7c93a6 14%, #3f5a2c 24%, var(--foliage-mid) 45%, var(--lawn) 65%, var(--foliage-dark) 100%);
  }
  .hero-shade { position: absolute; inset: 0; background: var(--shade); }

  .brand {
    position: absolute; left: 77px; top: 36px;
    font-size: 26px; font-weight: 500; letter-spacing: -0.2px;
  }
  .nav-link {
    position: absolute; left: 955px; top: 36px;
    font-size: 15px; font-weight: 500; color: var(--white); text-decoration: none;
  }
  .menu-toggle { position: absolute; left: 1101px; top: 35px; width: 32px; height: 22px; }
  .rail { position: absolute; left: 1074px; top: 0; width: 1px; height: 675px; background: rgba(255,255,255,0.75); }

  .project { position: absolute; left: 102px; top: 312px; }
  .project-kicker { font-size: 19px; font-weight: 300; color: var(--accent-green); letter-spacing: 0.2px; }
  .project-title { margin-top: 14px; font-size: 31px; font-weight: 600; letter-spacing: 0.1px; }
  .project-detail {
    display: flex; align-items: center; gap: 12px;
    margin-top: 38px; font-size: 14px; font-weight: 400; letter-spacing: 0.3px;
    color: var(--white); text-decoration: none;
  }
  .project-detail::before { content: ""; width: 20px; height: 1px; background: var(--white); margin-top: 8px; }

  .slider-controls { position: absolute; left: 887px; top: 528px; display: flex; gap: 16px; }
  .slider-btn { width: 54px; height: 54px; }
</style>
</head>
<body>
  <main class="hero">
    <div class="hero-photo" role="img" aria-label="Landscaped front garden with paved path, trimmed shrubs, a bench and a blue spruce beside a brick house"></div>
    <div class="hero-shade"></div>

    <div class="brand">Brookmoor Greens, Inc</div>
    <a class="nav-link" href="#">All Portfolio</a>
    <svg class="menu-toggle" viewBox="0 0 32 22" aria-label="Menu">
      <g stroke="#ffffff" stroke-width="2">
        <line x1="1" y1="1" x2="23" y2="1"/>
        <line x1="0" y1="11" x2="32" y2="11"/>
        <line x1="0" y1="21" x2="32" y2="21"/>
      </g>
    </svg>
    <div class="rail"></div>

    <section class="project">
      <p class="project-kicker">Portfolio</p>
      <h1 class="project-title">Landscaping house</h1>
      <a class="project-detail" href="#">DETAIL</a>
    </section>

    <div class="slider-controls">
      <svg class="slider-btn" viewBox="0 0 54 54" aria-label="Previous">
        <circle cx="27" cy="27" r="26" fill="none" stroke="#ffffff" stroke-width="1"/>
        <polyline points="30,20 23,27 30,34" fill="none" stroke="#ffffff" stroke-width="1.3"/>
      </svg>
      <svg class="slider-btn" viewBox="0 0 54 54" aria-label="Next">
        <circle cx="27" cy="27" r="26" fill="none" stroke="#ffffff" stroke-width="1"/>
        <polyline points="24,20 31,27 24,34" fill="none" stroke="#ffffff" stroke-width="1.3"/>
      </svg>
    </div>
  </main>
</body>
</html>
```